Velmora Interiors Stationary Set

Velmora Interiors is a bespoke interior design firm set to provide services to VIP clients with elegance and minimalism is the main theme for our stationary set. We require a full stationary set covering A4 letterhead, A4 & A3 envelopes, business cards, USB's, CDs, email signature and any other item the designer sees fit. logo is already designed and finalized, and we require the designer to use it as is without modifying the logo.

Address to be used on letterhead / business cards ...etc shall be as follows:

Phone : +971 2 518 3074
P.O. Box : 609318
Address: Block C&D, Bldg. 27, Court 14, Abu Dhabi, United Arab Emirates
Website: www.velmorainteriors-example.com

Target Market(s)

VIP Clients

Industry/Entity Type

Interior Design

Other font styles liked:
• something to be unique

Colors

Designer to choose colors to be used in the design.

Requirements
Must have
• Elegant, minimalistic
Nice to have
• Simple yet elegant design having a sharp yet clean cut format
Should not have
• No additional colours, just colours that are used in the logo (silver, black or gold)

```html
<!DOCTYPE html>
<html lang="en">
<head>
<meta charset="utf-8">
<title>Velmora Interiors – Business Card</title>
<link href="https://fonts.googleapis.com/css2?family=Crimson+Text:wght@400&family=Satisfy&display=swap" rel="stylesheet">
<style>
  :root {
    --backdrop: #1c1c1d;
    --card: #2a2a2b;
    --gold: #b89454;
    --gold-edge: #8a6d3b;
    --silver: #c9c9cb;
    --text-light: #e6e6e6;
    --rule: #8c8c8e;
  }
  * { margin: 0; padding: 0; box-sizing: border-box; }
  html, body {
    width: 1200px; height: 900px; overflow: hidden;
    background: var(--backdrop);
  }
  .stage {
    position: relative; width: 1200px; height: 900px;
  }
  .card {
    position: absolute; left: 250px;
    width: 700px; height: 400px;
    background: var(--card);
    border-bottom: 3px solid var(--gold-edge);
    border-left: 1px solid var(--gold-edge);
  }
  .card-front { top: 30px; }
  .card-back { top: 470px; }

  .brand {
    position: absolute; left: 0; right: 0; top: 168px;
    text-align: center;
    font-family: "Crimson Text", Georgia, serif;
    font-weight: 400;
    font-size: 38px;
    letter-spacing: 6px;
    color: var(--silver);
  }

  .identity {
    position: absolute; right: 375px; top: 200px;
    text-align: right;
  }
  .identity-name {
    font-family: "Satisfy", cursive;
    font-size: 27px;
    color: var(--gold);
    line-height: 1.1;
  }
  .identity-title {
    font-family: "Crimson Text", Georgia, serif;
    font-size: 19px;
    color: var(--text-light);
  }
  .divider {
    position: absolute; left: 345px; top: 185px;
    width: 1px; height: 150px;
    background: var(--rule);
  }
  .contact {
    position: absolute; left: 368px; top: 180px;
    font-family: "Crimson Text", Georgia, serif;
    font-size: 16px;
    line-height: 21px;
    color: var(--text-light);
  }
  .contact-address { margin-bottom: 6px; }
  .contact-row { display: flex; align-items: center; gap: 9px; }
  .contact-icon { width: 13px; height: 13px; fill: var(--gold); flex: none; }
</style>
</head>
<body>
<div class="stage">
  <section class="card card-front">
    <div class="brand">Velmora Interiors</div>
  </section>

  <section class="card card-back">
    <div class="identity">
      <div class="identity-name">Daniel Hartley</div>
      <div class="identity-title">President</div>
    </div>
    <div class="divider"></div>
    <div class="contact">
      <p class="contact-address">P.O. Box : 609318,<br>Block C&amp;D, Bldg. 27, Court 14<br>Abu Dhabi, United Arab Emirate</p>
      <p class="contact-row">
        <svg class="contact-icon" viewBox="0 0 24 24"><path d="M6.6 10.8a15.1 15.1 0 0 0 6.6 6.6l2.2-2.2a1 1 0 0 1 1-.25 11.4 11.4 0 0 0 3.6.57 1 1 0 0 1 1 1V20a1 1 0 0 1-1 1A17 17 0 0 1 3 4a1 1 0 0 1 1-1h3.5a1 1 0 0 1 1 1c0 1.25.2 2.45.57 3.57a1 1 0 0 1-.25 1z"/></svg>
        <span>+971 2 518 3074</span>
      </p>
      <p class="contact-row">
        <svg class="contact-icon" viewBox="0 0 24 24"><path d="M2 5h20v14H2z M3.5 6.5 12 12.5l8.5-6" fill="none" stroke="#b89454" stroke-width="2"/></svg>
        <span>info@velmorainteriors-example.com</span>
      </p>
      <p class="contact-row">
        <svg class="contact-icon" viewBox="0 0 24 24"><circle cx="12" cy="12" r="10"/><path d="M2 12h20M12 2c3 3 3 17 0 20M12 2c-3 3-3 17 0 20" fill="none" stroke="#2a2a2b" stroke-width="1.5"/></svg>
        <span>www.velmorainteriors-example.com</span>
      </p>
    </div>
  </section>
</div>
</body>
</html>
```